Full stationary package for an IT company specialized in personal cloud solutions
Corvanta Integrated Solutions SDN.BHD.
Full stationary package for an IT company specialized in personal cloud solutions - Information Technology
Creative Brief
Simple
Farid Al Mansoor
Managing Director
Jalan Taman Seroja Indah, No.8 Block F, 17B,2C
farid.mansoor@corvanta-example.com
www.corvanta-example.com
2864019 K
FULL STATIONARY PACKAGE DESIGN PLEASE
Only the LOGO

```html
<!DOCTYPE html>
<html lang="en">
<head>
<meta charset="utf-8">
<title>Corvanta Business Card</title>
<link rel="stylesheet" href="https://fonts.googleapis.com/css2?family=Oswald:wght@400;500;600&family=Roboto:wght@400;500&display=swap">
<style>
  :root {
    --stage: #e4e2df;
    --card-top: #f7f7f6;
    --card-mid: #eceff1;
    --card-bottom: #d9dde0;
    --orange-light: #f9a43a;
    --orange: #f47b20;
    --orange-deep: #ea4f1c;
    --blue: #1d5fa8;
    --blue-dark: #173f73;
    --ink: #3b3f44;
    --muted: #6f757b;
    --white: #ffffff;
  }
  * { box-sizing: border-box; margin: 0; padding: 0; }
  html, body {
    width: 1200px; height: 770px; overflow: hidden;
    background: var(--stage);
  }
  .canvas { position: relative; width: 1200px; height: 770px; }
  .card {
    position: absolute; left: 100px; top: 100px;
    width: 1000px; height: 570px;
    background: linear-gradient(180deg, var(--card-top) 0%, var(--card-mid) 55%, var(--card-bottom) 100%);
    box-shadow: 0 18px 40px rgba(0,0,0,.18);
    overflow: hidden;
    font-family: "Roboto", sans-serif;
  }
  .brand {
    position: absolute; left: 240px; top: 70px;
    display: flex; align-items: center; gap: 26px;
  }
  .brand-dot {
    width: 120px; height: 120px; border-radius: 50%;
    background: var(--orange);
  }
  .brand-name {
    font-family: "Oswald", sans-serif; font-weight: 500;
    font-size: 64px; letter-spacing: 4px; color: var(--blue);
  }
  .band {
    position: absolute; left: 0; top: 215px; width: 100%; height: 252px;
    background: linear-gradient(90deg, var(--orange-light) 0%, var(--orange) 45%, var(--orange-deep) 100%);
    border-top: 6px solid var(--blue);
    border-bottom: 6px solid var(--blue);
  }
  .band-item {
    position: absolute; top: 38px;
    display: flex; flex-direction: column; align-items: center;
    color: var(--white); text-align: center;
  }
  .band-item.person { left: 90px; width: 200px; }
  .band-item.web { left: 330px; width: 340px; }
  .band-item.phone { left: 700px; width: 220px; }
  .icon-ring {
    width: 90px; height: 90px; border-radius: 50%;
    background: rgba(255,255,255,.28);
    border: 3px solid rgba(255,255,255,.75);
    display: flex; align-items: center; justify-content: center;
    margin-bottom: 22px;
  }
  .person-name {
    font-family: "Oswald", sans-serif; font-weight: 500;
    font-size: 34px; letter-spacing: 1px; line-height: 1.1;
  }
  .person-role {
    font-size: 14px; letter-spacing: 2px; text-transform: uppercase; margin-top: 4px;
  }
  .contact-line { font-size: 21px; line-height: 32px; letter-spacing: .5px; }
  .footer {
    position: absolute; left: 0; top: 467px; width: 100%; height: 103px;
    border-bottom: 8px solid var(--blue);
  }
  .follow {
    position: absolute; left: 90px; top: 26px; color: var(--ink);
  }
  .follow-title {
    font-family: "Oswald", sans-serif; font-size: 28px; letter-spacing: 3px; line-height: 1;
  }
  .follow-sub {
    font-size: 11px; letter-spacing: 2px; color: var(--muted); margin-top: 6px;
  }
  .social {
    position: absolute; left: 330px; top: 34px;
    display: flex; gap: 22px;
  }
  .social-mark {
    width: 30px; height: 30px; border-radius: 50%; background: var(--blue-dark);
  }
</style>
</head>
<body>
<main class="canvas">
  <section class="card" aria-label="Corvanta business card">
    <header class="brand">
      <div class="brand-dot"></div>
      <div class="brand-name">CORVANTA</div>
    </header>

    <div class="band">
      <div class="band-item person">
        <div class="icon-ring">
          <svg width="46" height="46" viewBox="0 0 46 46" aria-hidden="true">
            <circle cx="23" cy="15" r="9" fill="#fff"/>
            <path d="M6 42c0-10 8-16 17-16s17 6 17 16z" fill="#fff"/>
          </svg>
        </div>
        <div class="person-name">ADAM REKHAN</div>
        <div class="person-role">General Manager</div>
      </div>

      <div class="band-item web">
        <div class="icon-ring">
          <svg width="50" height="50" viewBox="0 0 50 50" aria-hidden="true" fill="none" stroke="#fff" stroke-width="3">
            <circle cx="25" cy="25" r="20"/>
            <ellipse cx="25" cy="25" rx="9" ry="20"/>
            <line x1="5" y1="25" x2="45" y2="25"/>
            <path d="M9 14h32M9 36h32"/>
          </svg>
        </div>
        <div class="contact-line">adam@corvanta-example.com</div>
        <div class="contact-line">www.corvanta-example.com</div>
      </div>

      <div class="band-item phone">
        <div class="icon-ring">
          <svg width="30" height="48" viewBox="0 0 30 48" aria-hidden="true">
            <rect x="2" y="2" width="26" height="44" rx="4" fill="none" stroke="#fff" stroke-width="3"/>
            <rect x="6" y="8" width="18" height="28" fill="#fff"/>
            <circle cx="15" cy="41" r="2.2" fill="#fff"/>
          </svg>
        </div>
        <div class="contact-line">012 555 0189</div>
        <div class="contact-line">012 555 0189</div>
      </div>
    </div>

    <footer class="footer">
      <div class="follow">
        <div class="follow-title">FOLLOW US</div>
        <div class="follow-sub">ON SOCIAL NETWORKS</div>
      </div>
      <div class="social" aria-label="Social networks">
        <span class="social-mark"></span>
        <span class="social-mark"></span>
        <span class="social-mark"></span>
        <span class="social-mark"></span>
      </div>
    </footer>
  </section>
</main>
</body>
</html>
```